Brisk Treadway - Design Australia's largest Tyre ecommerce website!

We need a home page design and headers for the other pages.

Our site is built on magento community and is up and running at
brisktreadway.com.au
so you can see what we do. Basically all the elements on the current home page are required but don't have to stay in the current form. This is just a template we used to get the site functional with little regard to design.

We are the only tyre company in Australia that is 100% online. We sell tyres for almost every vehicle including motor bikes, cars, 4x4, trucks tractors, ATVs mining equipment. We have no shopfront, we dont fit tyres or run a shopfront. We just sell and ship tyres at the best prices possible.

We want a design that
* uses complimentary colours to our logo.
* has space for the video and tyre chooser - without scrolling the tyre chooser needs to be visible at least in part. The chooser is a key element. This is how most customers will find their tyre.
* in the header or somewhere prominent on the homepage we want to advertise
Australia Wide Delivery
Free delivery to Brisbane Sydney Melbourne
$20 to all other locations **with few exceptions (the small print)
Fast Delivery to your door -
1-3 Business days to most metro areas
5-10 Business days to all other areas **With few exceptions

On the home page we also want
* links to our facebook and twitter accounts
* a specials banner/space, with space to display up to 20 items.
* customer testimonials space

Thanks in advance!
Updates

Hi - It is in the job description but just to emphasise, the tyre chooser and intro video are key elements of our page and we need users to be drawn to them in a very visual way. Not flashing neon lights but some kind of elegant clean design. 

There are two paths a user may take - most will go straight to the tyre chooser to find their product. The rest will click on a category and then use the "shop by" filters to quickly refine their search.

Target Market(s)

18-30 Male retail. Truck and heavy equipment companies

Industry/Entity Type

Business

Requirements
Must have
• We want a design that
Australia Wide Delivery
Nice to have
• Possibly a graphic that indicates that we sell all tyres and not just cars and 4x4

```html
<!DOCTYPE html>
<html lang="en">
<head>
<meta charset="utf-8">
<title>Brisk Treadway – Online Tyre Company</title>
<link href="https://fonts.googleapis.com/css2?family=Open+Sans:wght@400;600;700&family=Lora:wght@400&display=swap" rel="stylesheet">
<style>
:root{
  --page:#f6f5f2;
  --panel:#ffffff;
  --line:#e4e3df;
  --text:#444444;
  --blue:#1767b1;
  --blue-bright:#0b73c4;
  --red:#c8201f;
  --nav-top:#7b7d80;
  --nav-bot:#55575a;
  --footer:#2b2b2b;
  --footer-bottom:#1e1e1e;
  --tyre:#2e3236;
  --tile:#eef1f5;
  --tile-edge:#d5dbe3;
}
*{box-sizing:border-box;margin:0;padding:0}
html,body{width:784px;height:1200px;overflow:hidden}
body{background:var(--page);font-family:"Open Sans",Arial,sans-serif;color:var(--text);position:relative;font-size:9px}
a{color:inherit;text-decoration:none}

.header{position:absolute;left:0;top:0;width:784px;height:84px;background:linear-gradient(#ffffff,#f3f3f3)}
.brand{position:absolute;left:86px;top:24px;display:flex;align-items:center;gap:8px}
.brand-mark{width:22px;height:22px;border-radius:50%;background:var(--tyre)}
.brand-name{font-size:19px;font-weight:700;color:var(--blue);letter-spacing:-.3px;line-height:1}
.brand-sub{position:absolute;left:116px;top:49px;font-size:6.5px;font-weight:600;color:#333;letter-spacing:.3px}
.top-links{position:absolute;top:13px;left:455px;display:flex}
.top-links a{display:block;font-size:8.5px;color:#333;padding:0 0 6px 0;border-bottom:2px solid #999;margin-right:18px}
.top-links a.on{border-color:var(--blue)}
.top-links a:nth-child(1){width:58px}
.top-links a:nth-child(2){width:52px}
.top-links a:nth-child(3){width:55px}
.top-links a:nth-child(4){width:42px;margin-right:0}
.experts{position:absolute;left:498px;top:44px;font-family:"Lora",serif;font-size:8px;color:var(--blue);letter-spacing:.3px}
.phone{position:absolute;left:480px;top:57px;font-family:"Lora",serif;font-size:14px;color:#222;display:flex;align-items:center;gap:5px}
.phone span{color:var(--red)}
.cart-icon{position:absolute;left:612px;top:44px}
.cart-text{position:absolute;left:662px;top:47px;font-size:8px;line-height:12px;color:#333}
.cart-text b{color:var(--blue);font-weight:400;font-size:9px}

.mainnav{position:absolute;left:85px;top:101px;width:614px;height:27px;background:linear-gradient(var(--nav-top),var(--nav-bot));display:flex;align-items:center;justify-content:space-between;padding:0 10px;border-radius:2px}
.mainnav a{color:#fff;font-size:8.2px}

.cats{position:absolute;left:85px;top:143px;width:144px;list-style:none}
.cats li{height:30.7px;display:flex;align-items:center;background:linear-gradient(#fbfbfa,#f1f0ed);border-bottom:1px solid #fff;font-size:8.5px;color:#555}
.cats li svg{margin:0 14px 0 18px}
.view-more{position:absolute;left:126px;top:430px;font-size:8px;font-style:italic;font-weight:600;color:var(--blue)}

.hero{position:absolute;left:242px;top:142px;width:457px;height:288px;background:#fff;border:1px solid var(--line)}
.hero-media{position:absolute;left:4px;top:4px;width:449px;height:280px;background:linear-gradient(100deg,#1f2225 0%,#34383c 45%,#6b5446 65%,#c87a3c 100%)}
.dots{position:absolute;right:5px;bottom:4px;display:flex;gap:4px}
.dots i{width:9px;height:9px;background:#888;display:block}
.dots i.on{background:var(--blue)}

.panel{position:absolute;background:var(--panel);border:1px solid var(--line)}
.title{font-size:12.5px;color:var(--blue);font-weight:400;letter-spacing:.1px}
.chooser{left:85px;top:483px;width:458px;height:271px}
.chooser .title{position:absolute;left:15px;top:11px}
.chooser p{position:absolute;left:16px;top:40px;width:408px;font-size:8.3px;line-height:13px;color:#333}
.tab{position:absolute;top:98px;height:21px;font-size:8.5px;font-weight:600;color:#fff;display:flex;align-items:center;justify-content:center}
.tab.metric{left:16px;width:59px;background:linear-gradient(#2a80cf,#0e559b)}
.tab.standard{left:80px;width:60px;background:linear-gradient(#8a8c8f,#5f6164)}
.tyre-pic{position:absolute;left:13px;top:144px;width:139px;height:90px;background:linear-gradient(90deg,#e9eaec,#c9ccd0 40%,#2e3236 70%,#1c1e20)}
.field{position:absolute;font-size:8.2px;color:#333}
.select{position:absolute;width:75px;height:14px;background:#fff;border:1px solid #d6d6d6}
.select::after{content:"";position:absolute;right:2px;top:2px;width:9px;height:8px;background:#cfe0f2}
.find{position:absolute;left:366px;top:241px;width:71px;height:19px;background:linear-gradient(#8a8c8f,#5f6164);color:#fff;font-size:8.2px;font-weight:600;display:flex;align-items:center;justify-content:center}

.info{left:555px;top:483px;width:144px;height:271px}
.info-head{position:absolute;left:-1px;top:-1px;width:144px;height:24px;background:linear-gradient(#1180d2,#0a5ca8);color:#fff;font-size:10px;font-weight:600;padding:5px 11px}
.info ul{position:absolute;left:8px;top:34px;width:128px;list-style:none}
.info li{position:relative;padding:6px 0 6px 18px;border-bottom:1px solid var(--line);font-size:8px;line-height:16px;color:#333}
.info li:last-child{border-bottom:0}
.info li svg{position:absolute;left:2px;top:12px}

.brands{left:85px;top:789px;width:614px;height:217px}
.brands .title{position:absolute;left:13px;top:13px}
.arrows{position:absolute;left:569px;top:15px;display:flex;gap:5px}
.brands .lead{position:absolute;left:14px;top:42px;width:418px;font-size:8.3px;line-height:17px;color:#333}
.logo-box{position:absolute;top:89px;height:40px;display:flex;align-items:center;justify-content:center;font-weight:600;font-size:12px;background:var(--tile);border:1px solid var(--tile-edge);color:var(--blue)}
.bname{position:absolute;top:137px;font-size:9.5px;color:var(--blue)}
.bdesc{position:absolute;top:161px;font-size:7.5px;line-height:12px;color:#444}

.footer{position:absolute;left:0;top:1032px;width:784px;height:126px;background:var(--footer)}
.fcol{position:absolute;top:26px}
.fcol h4{font-size:11px;font-weight:400;color:#e8e8e8;margin-bottom:10px}
.fcol ul{list-style:none}
.fcol li{font-size:8px;color:#ddd;height:17px;display:flex;align-items:center;gap:9px}
.search{position:absolute;left:506px;top:24px;width:190px;height:48px;background:var(--blue-bright);padding:6px 8px}
.search span{color:#fff;font-size:8.5px}
.search .box{position:absolute;left:8px;top:24px;width:114px;height:17px;background:#fff}
.search .btn{position:absolute;left:127px;top:24px;width:53px;height:17px;background:#0a4f95;color:#fff;font-size:7.5px;display:flex;align-items:center;justify-content:center}
.social{position:absolute;left:614px;top:92px;display:flex;gap:5px}
.social i{display:block;width:16px;height:16px;border-radius:3px;background:#5b5e62}
.fbottom{position:absolute;left:0;top:1158px;width:784px;height:42px;background:var(--footer-bottom)}
.copy{position:absolute;left:87px;top:15px;font-size:7.5px;color:#ddd}
.pay{position:absolute;left:642px;top:11px;width:54px;height:21px;background:#44474b;border-radius:2px;display:flex;align-items:center;justify-content:center;font-size:8px;font-weight:600;color:#e8e8e8}
</style>
</head>
<body>

<header class="header">
  <div class="brand"><span class="brand-mark"></span><span class="brand-name">BRISK TREADWAY</span></div>
  <div class="brand-sub">YOUR ONLINE TYRE COMPANY</div>
  <nav class="top-links">
    <a class="on" href="#">My Account</a><a class="on" href="#">Checkout</a><a href="#">My Wishlist</a><a href="#">Log In</a>
  </nav>
  <div class="experts">ASK OUR EXPERTS</div>
  <div class="phone">
    <svg width="11" height="11" viewBox="0 0 24 24"><path fill="#c8201f" d="M6.6 10.8a15.1 15.1 0 0 0 6.6 6.6l2.2-2.2c.3-.3.7-.4 1-.2 1.1.4 2.3.6 3.6.6.6 0 1 .4 1 1V20c0 .6-.4 1-1 1A17 17 0 0 1 3 4c0-.6.4-1 1-1h3.5c.6 0 1 .4 1 1 0 1.3.2 2.5.6 3.6.1.3 0 .7-.2 1z"/></svg>
    <span>0400 217 934</span>
  </div>
  <svg class="cart-icon" width="38" height="30" viewBox="0 0 38 30">
    <path d="M2 4h6l4 16h20l4-12H10" fill="none" stroke="#b81e1e" stroke-width="2.5" stroke-linejoin="round"/>
    <rect x="11" y="8" width="23" height="10" fill="#d83a32"/>
    <circle cx="14" cy="25" r="3" fill="#333"/><circle cx="29" cy="25" r="3" fill="#333"/>
  </svg>
  <div class="cart-text"><b>Cart</b><br>0 item(s)</div>
</header>

<nav class="mainnav">
  <a href="#">About Us</a><a href="#">Customer Service</a><a href="#">Privacy Policy</a><a href="#">Site Map</a><a href="#">Search Terms</a><a href="#">Advanced Search</a><a href="#">Orders and Returns</a><a href="#">Contact Us</a>
</nav>

<ul class="cats">
  <li><svg width="8" height="6" viewBox="0 0 8 6"><path d="M0 3h7M4.5 .5L7 3 4.5 5.5" stroke="#c8201f" fill="none" stroke-width="1.2"/></svg>Car</li>
  <li><svg width="8" height="6" viewBox="0 0 8 6"><path d="M0 3h7M4.5 .5L7 3 4.5 5.5" stroke="#c8201f" fill="none" stroke-width="1.2"/></svg>4x4</li>
  <li><svg width="8" height="6" viewBox="0 0 8 6"><path d="M0 3h7M4.5 .5L7 3 4.5 5.5" stroke="#c8201f" fill="none" stroke-width="1.2"/></svg>Light Truck</li>
  <li><svg width="8" height="6" viewBox="0 0 8 6"><path d="M0 3h7M4.5 .5L7 3 4.5 5.5" stroke="#c8201f" fill="none" stroke-width="1.2"/></svg>Truck</li>
  <li><svg width="8" height="6" viewBox="0 0 8 6"><path d="M0 3h7M4.5 .5L7 3 4.5 5.5" stroke="#c8201f" fill="none" stroke-width="1.2"/></svg>Agriculture/OTR</li>
  <li><svg width="8" height="6" viewBox="0 0 8 6"><path d="M0 3h7M4.5 .5L7 3 4.5 5.5" stroke="#c8201f" fill="none" stroke-width="1.2"/></svg>Motorbike</li>
  <li><svg width="8" height="6" viewBox="0 0 8 6"><path d="M0 3h7M4.5 .5L7 3 4.5 5.5" stroke="#c8201f" fill="none" stroke-width="1.2"/></svg>Trailer/Caravan</li>
  <li><svg width="8" height="6" viewBox="0 0 8 6"><path d="M0 3h7M4.5 .5L7 3 4.5 5.5" stroke="#c8201f" fill="none" stroke-width="1.2"/></svg>Rims</li>
  <li><svg width="8" height="6" viewBox="0 0 8 6"><path d="M0 3h7M4.5 .5L7 3 4.5 5.5" stroke="#c8201f" fill="none" stroke-width="1.2"/></svg>Tubes</li>
</ul>
<a class="view-more" href="#">View More...</a>

<section class="hero">
  <div class="hero-media" role="img" aria-label="Photo of a smiling woman holding a stack of black tyres on a warehouse shelf"></div>
  <div class="dots"><i class="on"></i><i></i><i></i><i></i></div>
</section>

<section class="panel chooser">
  <h2 class="title">TYRE CHOOSER</h2>
  <p>Please select from the boxes to find your Tyres. On the left side you can filter by size and on the right side you can filter by brand. At anytime you can click on "Find My Tyres" to display the results of your selections.</p>
  <div class="tab metric">Metric</div>
  <div class="tab standard">Standard</div>
  <div class="tyre-pic" role="img" aria-label="Close-up of a tyre sidewall showing the size marking 205/55 R16"></div>
  <span class="field" style="left:165px;top:156px">Width</span>
  <span class="field" style="left:165px;top:182px;line-height:13px">Profile or<br>Height</span>
  <span class="field" style="left:165px;top:222px">Rim</span>
  <div class="select" style="left:213px;top:154px"></div>
  <div class="select" style="left:213px;top:181px"></div>
  <div class="select" style="left:213px;top:220px"></div>
  <span class="field" style="left:306px;top:156px">Brand</span>
  <span class="field" style="left:306px;top:182px">Vehicle</span>
  <span class="field" style="left:306px;top:208px">Accessories</span>
  <div class="select" style="left:360px;top:154px"></div>
  <div class="select" style="left:360px;top:180px"></div>
  <div class="select" style="left:360px;top:206px"></div>
  <div class="find">Find My Tyres</div>
</section>

<aside class="panel info">
  <div class="info-head">INFORMATION..</div>
  <ul>
    <li><svg width="8" height="6" viewBox="0 0 8 6"><path d="M0 3h7M4.5 .5L7 3 4.5 5.5" stroke="#c8201f" fill="none" stroke-width="1.2"/></svg>Australia Wide Delivery</li>
    <li><svg width="8" height="6" viewBox="0 0 8 6"><path d="M0 3h7M4.5 .5L7 3 4.5 5.5" stroke="#c8201f" fill="none" stroke-width="1.2"/></svg>Free delivery to Brisbane Sydney Melbourne</li>
    <li><svg width="8" height="6" viewBox="0 0 8 6"><path d="M0 3h7M4.5 .5L7 3 4.5 5.5" stroke="#c8201f" fill="none" stroke-width="1.2"/></svg>$20 to all other locations<br>Fast Delivery to your door</li>
    <li><svg width="8" height="6" viewBox="0 0 8 6"><path d="M0 3h7M4.5 .5L7 3 4.5 5.5" stroke="#c8201f" fill="none" stroke-width="1.2"/></svg>1-3 Business days to most metro areas</li>
    <li><svg width="8" height="6" viewBox="0 0 8 6"><path d="M0 3h7M4.5 .5L7 3 4.5 5.5" stroke="#c8201f" fill="none" stroke-width="1.2"/></svg>5-10 Business days to all other areas</li>
  </ul>
</aside>

<section class="panel brands">
  <h2 class="title">OUR VARIOUS BRANDS</h2>
  <div class="arrows">
    <svg width="13" height="13" viewBox="0 0 13 13"><circle cx="6.5" cy="6.5" r="6" fill="#eee" stroke="#aaa"/><path d="M7.5 4L5 6.5 7.5 9" stroke="#222" stroke-width="1.4" fill="none"/></svg>
    <svg width="13" height="13" viewBox="0 0 13 13"><circle cx="6.5" cy="6.5" r="6" fill="#eee" stroke="#aaa"/><path d="M5.5 4L8 6.5 5.5 9" stroke="#222" stroke-width="1.4" fill="none"/></svg>
  </div>
  <p class="lead">Lorem ipsum dolor sit amet, consectetur adipiscing elit. Praesent at augue eu tortor aliquet elementum at id sem. In ac ullamcorper eros.</p>

  <div class="logo-box" style="left:13px;width:76px">Tarrow</div>
  <div class="logo-box" style="left:100px;width:110px">Pellin</div>
  <div class="logo-box" style="left:221px;width:108px">Arvo</div>
  <div class="logo-box" style="left:341px;width:128px">Quillan</div>
  <div class="logo-box" style="left:481px;width:119px">Bexley</div>

  <span class="bname" style="left:23px">Tarrow</span>
  <span class="bname" style="left:110px">Pellin</span>
  <span class="bname" style="left:229px">Arvo</span>
  <span class="bname" style="left:349px">Quillan</span>
  <span class="bname" style="left:490px">Bexley</span>

  <span class="bdesc" style="left:14px;width:80px">Lorem ipsum dolor sit amet, consect-etur adip.</span>
  <span class="bdesc" style="left:105px;width:100px">Lorem ipsum dolor sit amet, consectetur adip dolor.</span>
  <span class="bdesc" style="left:223px;width:100px">Lorem ipsum dolor sit amet, consectetur adip dolor.</span>
  <span class="bdesc" style="left:343px;width:115px">Lorem ipsum dolor sit amet, consectetur adip dolor.</span>
  <span class="bdesc" style="left:488px;width:115px">Lorem ipsum dolor sit amet, consectetur adip dolor.</span>
</section>

<footer class="footer">
  <div class="fcol" style="left:90px">
    <h4>Why buy from us</h4>
    <ul>
      <li><svg width="5" height="7" viewBox="0 0 5 7"><path d="M1 1l2.5 2.5L1 6" stroke="#1c8fe0" stroke-width="1.3" fill="none"/></svg>Shipping &amp; Returns</li>
      <li><svg width="5" height="7" viewBox="0 0 5 7"><path d="M1 1l2.5 2.5L1 6" stroke="#1c8fe0" stroke-width="1.3" fill="none"/></svg>Secure Shopping</li>
    </ul>
  </div>
  <div class="fcol" style="left:239px">
    <h4>My account</h4>
    <ul>
      <li><svg width="5" height="7" viewBox="0 0 5 7"><path d="M1 1l2.5 2.5L1 6" stroke="#1c8fe0" stroke-width="1.3" fill="none"/></svg>&nbsp;Sign In</li>
      <li><svg width="5" height="7" viewBox="0 0 5 7"><path d="M1 1l2.5 2.5L1 6" stroke="#1c8fe0" stroke-width="1.3" fill="none"/></svg>&nbsp;View Cart</li>
      <li><svg width="5" height="7" viewBox="0 0 5 7"><path d="M1 1l2.5 2.5L1 6" stroke="#1c8fe0" stroke-width="1.3" fill="none"/></svg>&nbsp;My Wishlist</li>
    </ul>
  </div>
  <div class="fcol" style="left:348px">
    <h4>Brisk Treadway</h4>
    <ul>
      <li><svg width="5" height="7" viewBox="0 0 5 7"><path d="M1 1l2.5 2.5L1 6" stroke="#1c8fe0" stroke-width="1.3" fill="none"/></svg>&nbsp;No Risk Guarantee</li>
      <li><svg width="5" height="7" viewBox="0 0 5 7"><path d="M1 1l2.5 2.5L1 6" stroke="#1c8fe0" stroke-width="1.3" fill="none"/></svg>&nbsp;High Rollers</li>
      <li><svg width="5" height="7" viewBox="0 0 5 7"><path d="M1 1l2.5 2.5L1 6" stroke="#1c8fe0" stroke-width="1.3" fill="none"/></svg>&nbsp;FAQ</li>
    </ul>
  </div>
  <div class="search">
    <span>Find Something..</span>
    <div class="box"></div>
    <div class="btn">SEARCH</div>
  </div>
  <div class="social"><i></i><i></i><i></i><i></i></div>
</footer>
<div class="fbottom">
  <span class="copy">© 2013 Brisk Treadway. All Rights Reserved.</span>
  <div class="pay">Tendra</div>
</div>

</body>
</html>
```